Bill board design For Marlowe’s Construction

Billboard Design Request
Please design the billboard to match the branding, colors, and overall feel of our website: Marlowe's Construction Website
MARLOWE’S CONSTRUCTION
CONCRETE BUILT FOR GENERATIONS
⭐ 5-Star Rated on Zorvix
Please Include:
* All three attached project photos
* Company logo(s)
* Phone Number: 555-214-7630
* Website: MarlowesConstruction.example
* Zorvix logo with 5-star rating graphic
* Chatterly logo
* Pixtoria logo
Service Area:
Alderbrook • Fenwick Falls • Quarryton • Bellmere Hill
Please arrange the photos and layout in whatever way creates the strongest visual impact and readability from the road. The company name, headline, phone number, and website should be highly visible at highway speeds.
The overall appearance should be clean, professional, premium, and consistent with our website branding while highlighting our reputation, craftsmanship, and quality concrete work.
People Driving By
Concrete Construction

```html
<!DOCTYPE html>
<html lang="en">
<head>
<meta charset="utf-8">
<title>Marlowe’s Construction – Concrete Billboard</title>
<link rel="stylesheet" href="https://fonts.googleapis.com/css2?family=Montserrat:wght@600;700;800&family=Bebas+Neue&display=swap">
<style>
  :root {
    --brand-blue: #1e90e8;
    --ink: #050505;
    --white: #ffffff;
    --steel: #6d6d70;
    --star: #f5b50a;
    --page: #eef1f4;
  }
  * { margin: 0; padding: 0; box-sizing: border-box; }
  html, body { width: 1191px; height: 1200px; overflow: hidden; background: var(--page); }
  .billboard {
    position: absolute; left: 0; top: 373px;
    width: 1191px; height: 453px;
    background: var(--ink);
    overflow: hidden;
  }
  .header-band { position: absolute; left: 0; top: 0; width: 1191px; height: 152px; background: var(--ink); }
  .brand { position: absolute; left: 23px; top: 18px; display: flex; align-items: center; gap: 28px; }
  .brand-mark { width: 142px; height: 112px; background: var(--brand-blue); }
  .brand-name { font-family: "Montserrat", sans-serif; font-weight: 700; line-height: 1; }
  .brand-name .primary { display: block; font-size: 54px; letter-spacing: 1px; color: var(--brand-blue); }
  .brand-name .secondary {
    display: block; font-size: 14px; letter-spacing: 13.5px; margin-top: 12px;
    color: var(--steel); white-space: nowrap;
  }
  .headline {
    position: absolute; left: 633px; top: 20px; width: 520px; text-align: center;
    font-family: "Montserrat", sans-serif; font-weight: 800; color: var(--white);
    font-size: 88px; line-height: 1; letter-spacing: 1px;
  }
  .tagline {
    position: absolute; left: 700px; top: 104px; width: 410px;
    display: flex; align-items: center; justify-content: center; gap: 10px;
    font-family: "Montserrat", sans-serif; font-weight: 700; color: var(--white);
    font-size: 18px; letter-spacing: 1px;
  }
  .tagline-rule { height: 4px; width: 54px; background: var(--white); clip-path: polygon(0 50%, 100% 0, 100% 100%); }
  .tagline-rule.right { clip-path: polygon(0 0, 100% 50%, 0 100%); }
  .project-strip { position: absolute; left: 0; top: 152px; width: 1191px; height: 190px; }
  .service-bar {
    position: absolute; left: 0; top: 342px; width: 760px; height: 52px;
    background: var(--brand-blue);
    clip-path: polygon(0 0, 100% 0, 97% 100%, 0 100%);
    display: flex; align-items: center; padding-left: 42px; gap: 16px;
  }
  .service-areas {
    font-family: "Bebas Neue", sans-serif; color: var(--white); font-size: 33px;
    line-height: 1; padding-top: 4px; letter-spacing: 0.2px; white-space: nowrap;
  }
  .proof-bar {
    position: absolute; left: 0; top: 394px; width: 737px; height: 59px;
    background: var(--white);
    clip-path: polygon(0 0, 100% 0, 97% 100%, 0 100%);
  }
  .review-name {
    position: absolute; left: 116px; top: 13px;
    font-family: "Montserrat", sans-serif; font-weight: 700; font-size: 27px; color: var(--steel);
  }
  .stars { position: absolute; left: 230px; top: 14px; }
  .follow {
    position: absolute; left: 390px; top: 19px;
    font-family: "Bebas Neue", sans-serif; font-size: 21px; color: var(--ink);
    display: flex; align-items: center; gap: 8px;
  }
  .social { display: flex; align-items: center; gap: 4px; font-family: "Montserrat", sans-serif; font-weight: 700; font-size: 12px; color: var(--brand-blue); }
  .social-dot { width: 14px; height: 14px; border-radius: 50%; background: var(--brand-blue); }
  .contact { position: absolute; left: 760px; top: 342px; width: 431px; height: 111px; }
  .website {
    position: absolute; right: 34px; top: 8px;
    font-family: "Montserrat", sans-serif; font-weight: 700; font-size: 19.5px; color: var(--white);
  }
  .phone-icon { position: absolute; left: 7px; top: 45px; }
  .phone {
    position: absolute; right: 32px; top: 36px;
    font-family: "Bebas Neue", sans-serif; font-size: 70px; line-height: 1; color: var(--brand-blue);
    letter-spacing: 0.5px;
  }
</style>
</head>
<body>
<main class="billboard">
  <header class="header-band">
    <div class="brand">
      <div class="brand-mark"></div>
      <div class="brand-name">
        <span class="primary">MARLOWE’S</span>
        <span class="secondary">CONSTRUCTIONLLC</span>
      </div>
    </div>
    <h1 class="headline">CONCRETE</h1>
    <p class="tagline"><span class="tagline-rule"></span>BUILT FOR GENERATIONS<span class="tagline-rule right"></span></p>
  </header>

  <svg class="project-strip" width="1191" height="190" viewBox="0 0 1191 190">
    <defs>
      <linearGradient id="crew-tones" x1="0" y1="0" x2="1" y2="1">
        <stop offset="0" stop-color="#6b6a52"/>
        <stop offset="0.45" stop-color="#3d3f36"/>
        <stop offset="0.8" stop-color="#9a7a5a"/>
        <stop offset="1" stop-color="#b3463a"/>
      </linearGradient>
      <linearGradient id="walkway-tones" x1="0" y1="0" x2="0" y2="1">
        <stop offset="0" stop-color="#6f6c4c"/>
        <stop offset="0.35" stop-color="#5c6a34"/>
        <stop offset="0.6" stop-color="#a7653e"/>
        <stop offset="1" stop-color="#c9855a"/>
      </linearGradient>
      <linearGradient id="garage-tones" x1="0" y1="0" x2="0" y2="1">
        <stop offset="0" stop-color="#5f7d43"/>
        <stop offset="0.45" stop-color="#7a6a66"/>
        <stop offset="0.75" stop-color="#8a9a5a"/>
        <stop offset="1" stop-color="#d9d2c6"/>
      </linearGradient>
    </defs>
    <rect width="1191" height="190" fill="var(--steel)"/>
    <polygon points="0,5 432,5 400,185 0,185" fill="url(#crew-tones)" role="img" aria-label="Crew member guiding a concrete pump hose on a residential job site"/>
    <polygon points="438,5 832,5 801,185 406,185" fill="url(#walkway-tones)" role="img" aria-label="Finished stamped concrete walkway leading to a house"/>
    <polygon points="838,5 1191,5 1191,185 807,185" fill="url(#garage-tones)" role="img" aria-label="Brick garage with new concrete driveway"/>
  </svg>

  <div class="service-bar">
    <svg width="26" height="34" viewBox="0 0 26 34" aria-hidden="true">
      <path d="M13 1C6.4 1 1.5 6 1.5 12.3 1.5 20.5 13 31 13 31s11.5-10.5 11.5-18.7C24.5 6 19.6 1 13 1z" fill="var(--ink)"/>
      <circle cx="13" cy="12" r="4.5" fill="var(--brand-blue)"/>
      <ellipse cx="13" cy="32" rx="10" ry="2" fill="var(--ink)"/>
    </svg>
    <p class="service-areas">ALDERBROOK • FENWICK FALLS • QUARRYTON • BELLMERE HILL</p>
  </div>

  <div class="proof-bar">
    <span class="review-name">Zorvix</span>
    <svg class="stars" width="148" height="30" viewBox="0 0 148 30" role="img" aria-label="Five star rating">
      <g fill="var(--star)">
        <polygon points="14,1 17.6,10.5 27.5,10.9 19.8,17.1 22.4,27 14,21.4 5.6,27 8.2,17.1 0.5,10.9 10.4,10.5"/>
        <polygon transform="translate(30 0)" points="14,1 17.6,10.5 27.5,10.9 19.8,17.1 22.4,27 14,21.4 5.6,27 8.2,17.1 0.5,10.9 10.4,10.5"/>
        <polygon transform="translate(60 0)" points="14,1 17.6,10.5 27.5,10.9 19.8,17.1 22.4,27 14,21.4 5.6,27 8.2,17.1 0.5,10.9 10.4,10.5"/>
        <polygon transform="translate(90 0)" points="14,1 17.6,10.5 27.5,10.9 19.8,17.1 22.4,27 14,21.4 5.6,27 8.2,17.1 0.5,10.9 10.4,10.5"/>
        <polygon transform="translate(120 0)" points="14,1 17.6,10.5 27.5,10.9 19.8,17.1 22.4,27 14,21.4 5.6,27 8.2,17.1 0.5,10.9 10.4,10.5"/>
      </g>
    </svg>
    <div class="follow">
      <span>FOLLOW US ON :</span>
      <span class="social"><span class="social-dot"></span>Chatterly</span>
      <span class="social"><span class="social-dot"></span>Pixtoria</span>
    </div>
  </div>

  <div class="contact">
    <p class="website">MarlowesConstruction.example</p>
    <svg class="phone-icon" width="46" height="46" viewBox="0 0 46 46" aria-hidden="true">
      <circle cx="23" cy="23" r="21" fill="var(--brand-blue)"/>
      <path d="M15 12c1.5-1 3-.8 3.8.6l2.3 4c.6 1.1.3 2.3-.7 3l-1.6 1.1c1 2.6 3 4.8 5.6 6l1.2-1.5c.8-1 2.1-1.2 3.1-.5l3.8 2.6c1.300.9 1.4 2.5.3 3.8-1.8 2.1-4.6 2.9-7.3 1.8-6.2-2.6-10.5-7.3-12.3-13.5-.7-2.6.1-5.700 1.8-7.4z" fill="var(--ink)"/>
    </svg>
    <p class="phone">555-214-7630</p>
  </div>
</main>
</body>
</html>
```